Simple Logo Design for Semi-Clear Plastic Frosted Card stock

Create a business card on frosted plastic. compliment existing logo elements with a tree trunk, roots, or seed at the lower half and the full logo both on the front.

Contact information will go on a solid portion of the back of this design since this card stock is semi-transparent.

It is important to consider this plastic card stock medium in your design. I found helpful tips and guides listed at velnacard.example: be careful to understand ink printed on plastic cards cannot have too much of a consistent print area or risks peeling and fine lines can easily scratch off.
Updates

2" x 3.5" 20PT Clear Plastic Business cards with Round corners Please get info or templates here: https://www.velnacard.example/product-detail/2-x-35-20pt-clear-plastic-business-cards-with-round-corners

Target Market(s)

Not for profit- religion

Industry/Entity Type

Business

Contact Information for Business Card

Must include complementary elements to the existing logo

Font styles to use
Decorative

Colors
000000

Requirements
Must have
• Elements of community, nature and oneness. Such as: seed, roots, tree trunk, etc.
• Three lines of space on the back for Name, Title, Phone Number.
Nice to have
• I like a light use of decorative elements
Should not have
• No eyes, from faces or animals.

```html
<!DOCTYPE html>
<html lang="en">
<head>
<meta charset="utf-8">
<title>Kindred Grove – Business Cards</title>
<link rel="stylesheet" href="https://fonts.googleapis.com/css2?family=Arimo:ital,wght@0,400;0,700;1,400&display=swap">
<style>
  :root {
    --backdrop: #2b2b2b;
    --teal: #1d7770;
    --leaf-green: #4a9a3c;
    --silver: #c9c9c9;
    --paper: #ffffff;
    --ink-soft: #e9f3f1;
    --ink-muted: #555555;
  }
  * { margin: 0; padding: 0; box-sizing: border-box; }
  html, body { width: 1200px; height: 990px; overflow: hidden; }
  body {
    background: var(--backdrop);
    position: relative;
    font-family: "Arimo", Arial, sans-serif;
  }
  .card {
    position: absolute;
    border-radius: 16px;
    overflow: hidden;
  }

  /* Shared brand name block */
  .brand {
    position: absolute;
    display: flex;
    flex-direction: column;
    align-items: center;
    color: var(--teal);
  }
  .brand-row { display: flex; align-items: center; gap: 12px; }
  .brand-dot { border-radius: 50%; background: var(--teal); flex: none; }
  .brand-name { font-weight: 400; white-space: nowrap; }
  .brand-tagline { font-size: 12px; letter-spacing: 1.5px; text-transform: uppercase; white-space: nowrap; margin-top: 8px; }
  .brand-url {
    position: absolute; left: 0; right: 0; bottom: 40px;
    text-align: center; font-size: 13px; letter-spacing: 3px;
  }

  /* Contact card */
  .card--contact { left: 250px; top: 60px; width: 700px; height: 400px; background: var(--paper); }
  .card--contact .card-bg { position: absolute; inset: 0; }
  .card--contact .brand { left: 20px; top: 162px; width: 290px; }
  .card--contact .brand-dot { width: 20px; height: 20px; }
  .card--contact .brand-name { font-size: 32px; }
  .card--contact .brand-tagline { font-size: 10px; letter-spacing: 1px; }

  .contact {
    position: absolute;
    left: 420px; top: 100px;
    color: var(--paper);
  }
  .contact-name { font-size: 30px; font-weight: 700; letter-spacing: 0.5px; }
  .contact-title { font-size: 18px; font-style: italic; color: var(--ink-soft); margin-top: 2px; }
  .contact-address { font-size: 17px; line-height: 1.25; margin-top: 20px; }
  .contact-lines { list-style: none; margin-top: 18px; font-size: 17px; line-height: 1.3; }
  .contact-lines li { display: flex; align-items: center; gap: 10px; }
  .contact-lines svg { width: 15px; height: 15px; fill: var(--paper); flex: none; }

  /* Logo cards */
  .card--teal { left: 60px; top: 540px; width: 520px; height: 297px; background: var(--teal); }
  .card--white { left: 620px; top: 540px; width: 520px; height: 297px; background: var(--paper); }
  .card--teal .brand, .card--white .brand { left: 0; right: 0; top: 108px; }
  .card--teal .brand-dot, .card--white .brand-dot { width: 20px; height: 20px; }
  .card--teal .brand-name, .card--white .brand-name { font-size: 38px; }
  .card--teal .brand { color: var(--paper); }
  .card--teal .brand-dot { background: var(--paper); }
  .card--teal .brand-url { color: var(--ink-soft); }
  .card--white .brand-url { color: var(--ink-muted); }
</style>
</head>
<body>

<section class="card card--contact" aria-label="Contact side">
  <svg class="card-bg" viewBox="0 0 700 400" preserveAspectRatio="none" aria-hidden="true">
    <path d="M318 0 C370 120 350 280 236 400" fill="none" stroke="var(--silver)" stroke-width="16"/>
    <path d="M338 0 C382 130 360 290 262 400" fill="none" stroke="var(--leaf-green)" stroke-width="8"/>
    <path d="M350 0 C396 130 376 290 282 400 L700 400 L700 0 Z" fill="var(--teal)"/>
  </svg>
  <div class="brand">
    <div class="brand-row"><span class="brand-dot"></span><span class="brand-name">Kindred Grove</span></div>
    <span class="brand-tagline">Rooted Together in Faith</span>
  </div>
  <div class="contact">
    <p class="contact-name">Elias Marlow</p>
    <p class="contact-title">Operations Manager</p>
    <p class="contact-address">Harbor Lane, St. No: 218<br>Sample text for location</p>
    <ul class="contact-lines">
      <li><svg viewBox="0 0 16 16"><path d="M3 1h3l1.5 4-2 1.3a9 9 0 0 0 4.2 4.2L11 8.5l4 1.5v3a2 2 0 0 1-2 2A13 13 0 0 1 1 3a2 2 0 0 1 2-2z"/></svg>000 555 0199</li>
      <li><svg viewBox="0 0 16 16"><path d="M1 3h14v10H1z M2 4l6 5 6-5" fill="none" stroke="#fff" stroke-width="1.5"/></svg>elias@kindredgrove.example</li>
      <li><svg viewBox="0 0 16 16"><circle cx="8" cy="8" r="6.5" fill="none" stroke="#fff" stroke-width="1.5"/><path d="M1.5 8h13M8 1.5c-3 3.5-3 9.5 0 13M8 1.5c3 3.5 3 9.5 0 13" fill="none" stroke="#fff" stroke-width="1.2"/></svg>www.kindredgrove.example</li>
    </ul>
  </div>
</section>

<section class="card card--teal" aria-label="Logo side, teal">
  <div class="brand">
    <div class="brand-row"><span class="brand-dot"></span><span class="brand-name">Kindred Grove</span></div>
    <span class="brand-tagline">Rooted Together in Faith</span>
  </div>
  <p class="brand-url">www.kindredgrove.example</p>
</section>

<section class="card card--white" aria-label="Logo side, white">
  <div class="brand">
    <div class="brand-row"><span class="brand-dot"></span><span class="brand-name">Kindred Grove</span></div>
    <span class="brand-tagline">Rooted Together in Faith</span>
  </div>
  <p class="brand-url">www.kindredgrove.example</p>
</section>

</body>
</html>
```